Edgy rebranded biz cards KRB

We are rebranding our 20 yr old mortgage company with a new logo and would like cards to compliment our new look.

Target Market(s)

potential home buyers or clients for refinance

Industry/Entity Type

Mortgage Brokerage

Contact Information for Business Card

418 W. Lomita Ave #305
Henderson, NV 89152
702.519.4827 o
702-519-4829 f
www.kestrelridgelending,example
nmls 842019
KRB is an equal housing lender

Font styles to use
Sans Serif

Colors
0455a3
3176b5
0393ce
33a6d7

Requirements
Must have
• space for a photo
Nice to have
• One side with the company info and the other with the person's info

```html
<!DOCTYPE html>
<html lang="en">
<head>
<meta charset="utf-8">
<title>Kestrel Ridge Lending – Business Card</title>
<link rel="stylesheet" href="https://fonts.googleapis.com/css2?family=Montserrat:wght@400;500;600;700&display=swap">
<style>
  :root {
    --brand-blue: #2a84f5;
    --ink-white: #ffffff;
    --page: #ffffff;
    --card-shadow: rgba(0, 0, 0, 0.22);
  }
  * { box-sizing: border-box; margin: 0; padding: 0; }
  html, body {
    width: 1200px;
    height: 1000px;
    overflow: hidden;
    background: var(--page);
    font-family: "Montserrat", Arial, sans-serif;
    color: var(--brand-blue);
  }
  .canvas { position: relative; width: 1200px; height: 1000px; }

  .card {
    position: absolute;
    left: 233px;
    width: 735px;
    height: 420px;
    background: var(--ink-white);
    box-shadow: 4px 5px 8px var(--card-shadow);
  }
  .card--front { top: 45px; }
  .card--back  { top: 535px; }

  .card__edges { position: absolute; inset: 0; width: 735px; height: 420px; }
  .card__edges polygon { fill: var(--brand-blue); }

  .text { position: absolute; line-height: 1; white-space: nowrap; }

  .brand-name {
    font-weight: 700;
    color: var(--brand-blue);
    text-align: center;
    line-height: 1.05;
    letter-spacing: 1px;
  }
  .card--front .brand-name { left: 0; width: 735px; top: 120px; font-size: 60px; }
  .card--back .brand-name  { left: 40px; width: 300px; top: 162px; font-size: 32px; }

  .website { left: 0; width: 735px; text-align: center; top: 341px; font-size: 22px; font-weight: 500; letter-spacing: 2.2px; }

  .lender-note { left: 40px; width: 300px; text-align: center; top: 307px; font-size: 20px; font-weight: 600; letter-spacing: 0.5px; }
  .nmls        { left: 40px; width: 300px; text-align: center; top: 346px; font-size: 18px; font-weight: 500; }

  .photo-marker { position: absolute; left: 292px; top: 23px; width: 152px; height: 350px; }
  .photo-marker circle.ring { fill: none; stroke: var(--brand-blue); stroke-width: 3; }
  .photo-marker circle.photo { fill: var(--brand-blue); }
  .photo-marker polygon { fill: var(--brand-blue); }

  .person-name  { left: 463px; top: 78px; font-size: 24px; font-weight: 700; }
  .person-role  { left: 463px; top: 108px; font-size: 18px; font-weight: 500; }
  .address-line { left: 393px; font-size: 19px; font-weight: 500; }
  .address-line--1 { top: 227px; }
  .address-line--2 { top: 251px; }
  .contact-line { left: 393px; font-size: 19px; font-weight: 500; }
  .contact-line--phone { top: 303px; }
  .contact-line--fax   { top: 347px; }
  .contact-label { display: inline-block; width: 72px; }
</style>
</head>
<body>
<div class="canvas">

  <section class="card card--front">
    <svg class="card__edges" viewBox="0 0 735 420" aria-hidden="true">
      <polygon points="0,0 14,0 2,420 0,420"/>
      <polygon points="733,0 735,0 735,420 721,420"/>
    </svg>
    <div class="text brand-name">Kestrel Ridge<br>Lending</div>
    <div class="text website">www.kestrelridgelending.example</div>
  </section>

  <section class="card card--back">
    <svg class="card__edges" viewBox="0 0 735 420" aria-hidden="true">
      <polygon points="0,0 2,0 14,420 0,420"/>
      <polygon points="721,0 735,0 735,420 733,420"/>
    </svg>

    <div class="text brand-name">Kestrel Ridge<br>Lending</div>
    <div class="text lender-note">EQUAL HOUSING LENDER</div>
    <div class="text nmls">Company NMLS 842019</div>

    <svg class="photo-marker" viewBox="0 0 152 350">
      <circle class="ring" cx="75" cy="74" r="72"/>
      <circle class="photo" cx="75" cy="74" r="62" role="img" aria-label="Portrait photo of the loan officer"/>
      <polygon points="71,146 79,146 77,345 72,345" aria-hidden="true"/>
    </svg>

    <div class="text person-name">Place for Name</div>
    <div class="text person-role">Owner</div>

    <div class="text address-line address-line--1">418 W Lomita Ave #305</div>
    <div class="text address-line address-line--2">Henderson, NV 89152</div>

    <div class="text contact-line contact-line--phone"><span class="contact-label">Phone</span>: 702-519-4827</div>
    <div class="text contact-line contact-line--fax"><span class="contact-label">Fax</span>: 702-519-4829</div>
  </section>

</div>
</body>
</html>
```